Home Services Website Design and Revisions

We have started to create a website but I would like to get some ideas and a quote on how to create a more professional website then what we have created thus far.

http://brindlehomeworks.example/

Pages I would need on the site

Home page - company summary and brand promise
who we are
what we do - services offered
our promise to quality and client experience
client experiences - testimonials and pictures
Promotions
Career opportunities - Join The team
Updates

Target Market(s)

Homeowners in the DFW region

Industry/Entity Type

Home Improvement

Number of Pages Required

5+ page

Font styles to use
Sans Serif

Requirements
Must have
• Home page - company summary and brand promise
• who we are
• what we do - services offered
• our promise to quality and client experience
• client experiences - testimonials and pictures
• Promotions
• Career opportunities - Join The team
• logo
• pictures
• links to social media sites
• A very impactful home page
• With a image of home and family.
• a beautiful home, yard and pictures of a loving family smiling and enjoying their home.
Nice to have
• Pictures with people to create emotion
• we don't work on houses
• we work on homes with families that trust us to provide quality services in a timely manner
• Families that trust us as their partner when they need work at their home with their family
Should not have
• low quality images or images just of homes

```html
<!DOCTYPE html>
<html lang="en">
<head>
<meta charset="utf-8">
<title>Brindle Home Services</title>
<link href="https://fonts.googleapis.com/css2?family=Open+Sans:ital,wght@0,400;0,600;0,700;0,800;1,400;1,600&display=swap" rel="stylesheet">
<style>
:root{
  --blue:#1f78c9;
  --blue-dark:#17619f;
  --green:#6cb83a;
  --green-dark:#58a02c;
  --ink:#2b2b2b;
  --muted:#555;
  --panel:#e8f1f9;
  --footer:#1d1d1d;
  --white:#fff;
}
*{box-sizing:border-box;margin:0;padding:0}
html,body{width:1200px;height:3896px;overflow:hidden}
body{font-family:"Open Sans",Arial,sans-serif;color:var(--ink);background:var(--white);position:relative}
.abs{position:absolute}
section,header,nav,footer{position:absolute;left:0;width:1200px}

/* top bar */
.topbar{top:0;height:26px;font-size:10px;font-weight:700}
.topbar .services-list{left:100px;top:7px;color:#444;letter-spacing:.3px}
.topbar .services-list b{color:var(--green)}
.topbar .follow{left:895px;top:6px;font-size:11px;color:#333}
.social{display:flex;gap:6px}
.social span{width:18px;height:18px;background:var(--blue);display:block}
.topbar .social{position:absolute;left:955px;top:4px}

/* header */
.site-header{top:26px;height:109px}
.contact-block{top:36px;display:flex;align-items:center;gap:10px}
.contact-block .label{font-size:13px;color:#333;font-weight:600}
.contact-block .value{font-size:15px;color:#222;font-weight:600}
.call{left:100px}
.mail{right:100px;text-align:right}
.icon-circle{width:44px;height:44px;border-radius:50%;background:var(--blue);display:flex;align-items:center;justify-content:center}
.brand{left:520px;width:160px;top:14px;height:121px;background:var(--white);text-align:center;z-index:2}
.brand .name{font-size:44px;font-weight:800;color:var(--ink);line-height:1;margin-top:34px;letter-spacing:1px}

/* nav */
.main-nav{top:135px;height:31px;background:var(--blue)}
.main-nav a{position:absolute;top:8px;color:var(--white);font-size:12px;font-weight:700;text-transform:uppercase;text-decoration:none}
.nav-gap{left:520px;width:160px;height:31px;background:var(--white)}

/* hero */
.hero{top:166px;height:535px;background:linear-gradient(120deg,#f2efe9 0%,#d9cfc2 35%,#b7a28a 55%,#e6e2dc 80%,#f4f3f1 100%)}
.hero::after{content:"";position:absolute;left:0;right:0;bottom:0;height:160px;background:linear-gradient(rgba(0,0,0,0),rgba(0,0,0,.45))}
.hero .tagline{left:0;width:1200px;top:430px;text-align:center;color:var(--white);font-size:35px;font-weight:800;line-height:44px;text-transform:uppercase;text-shadow:0 2px 4px rgba(0,0,0,.6);z-index:2}
.hero .arrow{top:220px;width:30px;height:30px;background:rgba(0,0,0,.6);z-index:2;display:flex;align-items:center;justify-content:center}

/* welcome */
.welcome{top:701px;height:403px}
.welcome h1{left:100px;top:64px;font-size:26px;font-weight:800;color:#333;display:flex;align-items:baseline;gap:10px}
.welcome h1 small{font-size:15px;font-weight:600;color:var(--muted)}
.welcome h1 .mark{width:18px;height:18px;background:var(--blue);display:inline-block;align-self:center}
.welcome p{left:100px;top:128px;width:660px;font-size:12.5px;line-height:19px;color:#333}
.btn{position:absolute;display:flex;align-items:center;justify-content:space-between;gap:10px;height:26px;padding:0 4px 0 14px;border-radius:13px;color:var(--white);font-size:12px;font-weight:600}
.btn i{width:20px;height:20px;border-radius:50%;background:rgba(0,0,0,.25);display:flex;align-items:center;justify-content:center}
.btn-green{background:var(--green)}
.btn-blue{background:var(--blue-dark)}
.inquiry{left:800px;top:42px;width:301px;height:317px;background:var(--panel)}
.inquiry h2{height:40px;background:var(--blue);color:var(--white);font-size:20px;font-weight:700;text-align:center;line-height:40px;letter-spacing:.5px}
.field{position:absolute;left:14px;width:273px;height:30px;background:var(--white);border:1px solid #cfd9e3;font-size:11px;color:#555;display:flex;align-items:center}
.field .ic{width:32px;height:100%;display:flex;align-items:center;justify-content:center;border-right:1px solid #dde4ea}
.field span.t{padding-left:10px}
.field.msg{height:60px;align-items:flex-start}
.field.msg .ic{height:30px;border-right:none}
.field.msg span.t{padding-top:8px}

/* who / what */
.intro-split{top:1104px;height:366px}
.half{top:0;height:366px;width:600px}
.half.who{left:0;background:var(--blue)}
.half.what{left:600px;background:var(--green)}
.half h2{position:absolute;top:42px;font-size:30px;font-weight:600;color:var(--white);display:flex;align-items:center;gap:10px}
.half p{position:absolute;top:100px;width:375px;font-size:12px;line-height:18px;color:var(--white);font-weight:600}
.seal{left:475px;top:60px;width:250px;height:250px;border-radius:50%;background:var(--white);border:10px solid rgba(255,255,255,.5);background-clip:padding-box;display:flex;align-items:center;justify-content:center;z-index:2}
.seal .name{font-size:44px;font-weight:800;color:var(--ink)}

/* services */
.services{top:1470px;height:719px;background:radial-gradient(ellipse at 50% 45%,#4c5a3a 0%,#2f3a26 45%,#1b2217 100%)}
.services h2{left:0;width:1200px;top:112px;text-align:center;color:var(--white);font-size:34px;font-weight:700;letter-spacing:1px}
.services .rule{top:135px;height:1px;width:330px;background:rgba(255,255,255,.5)}
.svc-icon{position:absolute;width:66px;height:66px;border-radius:50%;background:var(--blue);border:3px solid var(--white);display:flex;align-items:center;justify-content:center;z-index:2}
.svc-label{position:absolute;color:var(--white);font-size:14px;font-weight:700;line-height:19px;text-transform:uppercase}
.svc-label.l{text-align:right}
.services .center-name{left:480px;width:240px;top:578px;text-align:center;color:#cfcfcf;font-size:50px;font-weight:800;line-height:1}

/* gallery */
.gallery{top:2189px;height:974px;background:linear-gradient(#ffffff,#f1f1f1)}
.gallery h2{left:0;width:1200px;top:62px;text-align:center;font-size:34px;font-weight:700;color:#222}
.gallery h2 span{color:var(--blue)}
.gallery p{left:310px;width:580px;top:172px;text-align:center;font-size:12.5px;line-height:20px;color:#444}
.tile{position:absolute;width:331px;height:302px}
.tile-overlay{position:absolute;inset:0;background:rgba(20,20,20,.72);color:var(--white);text-align:center}
.tile-overlay h3{margin-top:105px;font-size:24px;font-weight:700;line-height:28px}
.tile-overlay p{position:static;width:auto;margin:14px 40px 0;font-size:13px;line-height:19px;color:#ddd}
.tile-overlay .plus{position:absolute;left:144px;top:232px;width:44px;height:44px;border-radius:50%;border:2px solid var(--white)}
.tile-overlay .plus::before,.tile-overlay .plus::after{content:"";position:absolute;background:var(--white);left:50%;top:50%;transform:translate(-50%,-50%)}
.tile-overlay .plus::before{width:18px;height:2px}
.tile-overlay .plus::after{width:2px;height:18px}

/* testimonial */
.testimonial{top:3163px;height:369px;background:linear-gradient(90deg,#5a5a5a,#7d7d7d 30%,#6b6b6b 60%,#858585 80%,#5c5c5c)}
.testimonial::before{content:"";position:absolute;inset:0;background:rgba(30,30,30,.45)}
.testimonial h2{left:0;width:1200px;top:42px;text-align:center;color:var(--white);font-size:34px;font-weight:700;z-index:1}
.avatar{left:104px;top:138px;width:124px;height:124px;border-radius:50%;background:linear-gradient(#e7d9c6,#b89e83);border:5px solid var(--white);z-index:1}
.quote{left:290px;top:165px;width:820px;color:var(--white);font-size:15px;font-style:italic;line-height:26px;z-index:1}
.quote b{font-size:30px;font-style:normal;font-weight:800;line-height:0;vertical-align:-8px;margin:0 4px}
.author{left:272px;top:282px;color:var(--white);font-size:13px;font-weight:700;z-index:1}
.dots{left:578px;top:316px;display:flex;gap:8px;z-index:1}
.dots span{width:11px;height:11px;border-radius:50%;background:var(--white)}
.dots span:first-child{background:var(--green)}

/* bottom nav */
.bottom-nav{top:3532px;height:68px;background:var(--green)}
.bottom-nav a{position:absolute;top:22px;color:var(--white);font-size:19px;text-decoration:none}

/* footer */
.site-footer{top:3600px;height:251px;background:linear-gradient(90deg,#1b1b1b,#262626 50%,#1c1c1c)}
.site-footer h4{position:absolute;top:34px;color:var(--white);font-size:16px;font-weight:600}
.quick-links{left:100px;top:76px;list-style:none}
.quick-links li{color:#ddd;font-size:13px;line-height:27px;padding-left:14px;position:relative}
.quick-links li::before{content:"";position:absolute;left:0;top:10px;border-left:6px solid var(--blue);border-top:4px solid transparent;border-bottom:4px solid transparent}
.info-row{position:absolute;left:338px;display:flex;gap:12px;color:#ddd;font-size:12.5px;line-height:19px}
.newsletter-note{left:655px;top:78px;width:190px;font-size:12px;line-height:18px;color:var(--green)}
.newsletter{left:655px;top:132px;display:flex}
.newsletter .input{width:170px;height:38px;background:#2e2e2e;border:1px solid #444;color:#888;font-size:12px;line-height:36px;padding-left:10px}
.newsletter .go{width:88px;height:38px;background:var(--blue);color:var(--white);font-size:13px;font-weight:600;text-align:center;line-height:38px}
.foot-brand{left:975px;top:40px;width:125px;text-align:center}
.foot-brand .name{color:var(--white);font-size:28px;font-weight:800}
.foot-brand .social{justify-content:center;margin-top:16px}
.copyright{top:3851px;height:45px;background:#111;color:#aaa;text-align:center;font-size:12px;line-height:45px}
</style>
</head>
<body>

<div class="topbar abs" style="top:0;left:0;width:1200px;height:26px">
  <div class="services-list abs"><b>•</b> PAINTING <b>•</b> LANDSCAPING/MOWING <b>•</b> WINDOW WASHING <b>•</b> MAID SERVICES</div>
  <div class="follow abs">Follow Us</div>
  <div class="social"><span></span><span></span><span></span><span></span></div>
</div>

<header class="site-header">
  <div class="contact-block call abs">
    <div class="icon-circle"><svg width="20" height="20" viewBox="0 0 24 24"><path fill="#fff" d="M6.6 10.8a15 15 0 006.6 6.6l2.2-2.2c.3-.3.7-.4 1-.2 1.1.4 2.3.6 3.6.6.6 0 1 .4 1 1V20c0 .6-.4 1-1 1A17 17 0 013 4c0-.6.4-1 1-1h3.5c.6 0 1 .4 1 1 0 1.3.2 2.5.6 3.6.1.3 0 .7-.2 1z"/></svg></div>
    <div><div class="label">CALL US</div><div class="value">555.010.2384</div></div>
  </div>
  <div class="brand abs"><div class="name">BRINDLE</div></div>
  <div class="contact-block mail abs">
    <div><div class="label">MAIL US</div><div class="value">hello@brindlehomeworks.example</div></div>
    <div class="icon-circle"><svg width="22" height="16" viewBox="0 0 22 16"><rect x="1" y="1" width="20" height="14" fill="none" stroke="#fff" stroke-width="2"/><path d="M1 1l10 8 10-8" fill="none" stroke="#fff" stroke-width="2"/></svg></div>
  </div>
</header>

<nav class="main-nav">
  <a style="left:100px">Who We Are</a>
  <a style="left:229px">What We Do</a>
  <a style="left:356px">Our Promise</a>
  <div class="nav-gap abs"></div>
  <a style="left:753px">Testimonials</a>
  <a style="left:904px">Promotions</a>
  <a style="left:1044px">Career</a>
</nav>

<section class="hero" role="img" aria-label="Smiling family of three relaxing together on a sofa in their bright living room">
  <div class="arrow abs" style="left:6px"><svg width="10" height="12"><path d="M8 1L2 6l6 5" fill="none" stroke="#fff" stroke-width="2"/></svg></div>
  <div class="arrow abs" style="right:6px"><svg width="10" height="12"><path d="M2 1l6 5-6 5" fill="none" stroke="#fff" stroke-width="2"/></svg></div>
  <div class="tagline abs">We are committed to providing reliable trusted<br>home services for you and your family.</div>
</section>

<section class="welcome">
  <h1 class="abs"><span class="mark"></span>WELCOME TO BRINDLE <small>PAINTING AND HOME SERVICES EXPERTS</small></h1>
  <p class="abs">Welcome To Brindle Home Services And Painting Specialists. We Are Committed To Providing Reliable TRUSTED Home Services For You And Your Family. We Are Home Service Experts With Decades Of Home Service Leadership And Expertise. Our Management Team Has Delivered Quality Services To Thousands Of Happy Families For Over 25 Years. We Take Pride In Delivering On Our Promises And Are Committed To Being Your Trusted Home Service Partner. A Partner That You Can Count On To Deliver Outstanding Quality As Promised. We Know That Finding A Trusted Contractor Is Often Difficult And Not The Way A Family Wants To Spend Their Precious Evenings And Weekends.</p>
  <div class="btn btn-green" style="left:100px;top:314px;width:130px">Read More <i><svg width="8" height="10"><path d="M1 1l5 4-5 4" fill="none" stroke="#fff" stroke-width="2"/></svg></i></div>

  <div class="inquiry abs">
    <h2>QUICK INQUIRY</h2>
    <div class="field" style="top:58px"><span class="ic"><svg width="12" height="12"><circle cx="6" cy="4" r="3" fill="#444"/><path d="M0 12a6 5 0 0112 0z" fill="#444"/></svg></span><span class="t">Name</span></div>
    <div class="field" style="top:100px"><span class="ic"><svg width="12" height="12" viewBox="0 0 24 24"><path fill="#444" d="M6.6 10.8a15 15 0 006.6 6.6l2.2-2.2c.3-.3.7-.4 1-.2 1.1.4 2.3.6 3.6.6.6 0 1 .4 1 1V20c0 .6-.4 1-1 1A17 17 0 013 4c0-.6.4-1 1-1h3.5c.6 0 1 .4 1 1 0 1.3.2 2.5.6 3.6.1.3 0 .7-.2 1z"/></svg></span><span class="t">Phone</span></div>
    <div class="field" style="top:142px"><span class="ic"><svg width="13" height="10"><rect x=".5" y=".5" width="12" height="9" fill="#444"/><path d="M.5 .5l6 5 6-5" fill="none" stroke="#fff"/></svg></span><span class="t">Email</span></div>
    <div class="field msg" style="top:184px"><span class="ic"><svg width="12" height="12"><rect x="1" y="1" width="10" height="10" fill="none" stroke="#444" stroke-width="1.5"/><path d="M4 8l5-5" stroke="#444" stroke-width="1.5"/></svg></span><span class="t">Message</span></div>
    <div class="btn btn-blue" style="left:14px;top:262px;width:104px">SUBMIT <i><svg width="8" height="10"><path d="M1 1l5 4-5 4" fill="none" stroke="#fff" stroke-width="2"/></svg></i></div>
  </div>
</section>

<section class="intro-split">
  <div class="half who abs">
    <h2 style="left:100px"><svg width="34" height="28" viewBox="0 0 34 28"><circle cx="9" cy="7" r="5" fill="#fff"/><circle cx="25" cy="7" r="5" fill="#fff"/><circle cx="17" cy="11" r="5" fill="#fff"/><path d="M0 26a9 9 0 0118 0zM16 26a9 9 0 0118 0zM8 28a9 9 0 0118 0z" fill="#fff"/></svg>Who We Are</h2>
    <p style="left:100px">Lorem ipsum dolor sit amet, consectetuer adipiscing elit, sed diam nonummy nibh euismod tincidunt ut laoreet dolore magna aliquam erat volutpat. Ut wisi enim ad minim veniam, quis nostrud exerci tation ullamcorper suscipit lobortis nisl ut aliquip ex ea commodo consequat. Duis autem vel eum iriure dolor in hendrerit in vulputate velit esse molestie consequat, vel illum dolore eu feugiat nulla facilisis at vero eros et accumsan et iusto odio dignissim qui blandit pr.</p>
    <div class="btn btn-green" style="left:100px;top:302px;width:130px">Read More <i><svg width="8" height="10"><path d="M1 1l5 4-5 4" fill="none" stroke="#fff" stroke-width="2"/></svg></i></div>
  </div>
  <div class="half what abs">
    <h2 style="left:250px"><svg width="28" height="28" viewBox="0 0 28 28"><path d="M4 14h5v12H4zM11 13l6-9c1-1 3 0 3 2l-1 6h6c2 0 3 2 2 3l-3 9c0 1-1 2-2 2H11z" fill="#fff"/></svg>What We Do</h2>
    <p style="left:160px;width:340px">Lorem ipsum dolor sit amet, consectetuer adipiscing elit, sed diam nonummy nibh euismod tincidunt ut laoreet dolore magna aliquam erat volutpat. Ut wisi enim ad minim veniam, quis nostrud exerci tation ullamcorper suscipit lobortis nisl ut aliquip ex ea commodo consequat. Duis autem vel eum iriure dolor in hendrerit in vulputate velit esse molestie consequat, vel illum dolore eu feugiat nulla facilisis at vero eros et accumsan et iusto odio dignissim.</p>
    <div class="btn btn-blue" style="left:372px;top:302px;width:128px">Read More <i><svg width="8" height="10"><path d="M1 1l5 4-5 4" fill="none" stroke="#fff" stroke-width="2"/></svg></i></div>
  </div>
  <div class="seal abs"><span class="name">BRINDLE</span></div>
</section>

<section class="services" role="img" aria-label="Dark evening view of a landscaped home garden behind the services diagram">
  <div class="rule abs" style="left:140px"></div>
  <h2 class="abs">OUR SERVICES</h2>
  <div class="rule abs" style="left:730px"></div>

  <svg class="abs" style="left:0;top:0" width="1200" height="719">
    <path d="M404 654 Q390 520 485 470 Q560 395 618 314 Q680 395 757 470 Q850 520 842 654" fill="none" stroke="rgba(255,255,255,.8)" stroke-width="2" stroke-dasharray="4 6"/>
  </svg>

  <div class="svc-label abs" style="left:518px;width:200px;top:220px;text-align:center">Interior &amp; Exterior<br>Residential Painting</div>
  <div class="svc-icon" style="left:585px;top:281px"><svg width="30" height="26"><path d="M3 13L15 3l12 10M7 11v12h16V11" fill="none" stroke="#fff" stroke-width="2.5"/></svg></div>

  <div class="svc-label l abs" style="left:290px;width:200px;top:379px">Junk Removal</div>
  <div class="svc-icon" style="left:505px;top:356px"><svg width="24" height="28"><path d="M2 6h20M8 6V2h8v4M5 6l2 20h10l2-20" fill="none" stroke="#fff" stroke-width="2.5"/></svg></div>

  <div class="svc-icon" style="left:668px;top:356px"><svg width="24" height="30"><circle cx="12" cy="5" r="4" fill="#fff"/><path d="M5 30V14a7 5 0 0114 0v16" fill="#fff"/></svg></div>
  <div class="svc-label abs" style="left:752px;width:260px;top:366px">General Labor Moving<br>Task &amp; Clean Up Chores</div>

  <div class="svc-label l abs" style="left:150px;width:250px;top:461px">Lawn Care Moving</div>
  <div class="svc-icon" style="left:422px;top:437px"><svg width="32" height="24"><path d="M2 16h22l4-8M4 16v-4h14v4" fill="none" stroke="#fff" stroke-width="2.5"/><circle cx="7" cy="20" r="3" fill="#fff"/><circle cx="20" cy="20" r="3" fill="#fff"/></svg></div>

  <div class="svc-icon" style="left:754px;top:437px"><svg width="32" height="24"><path d="M4 4v20M12 4v20M20 4v20M28 4v20M1 10h30M1 18h30" stroke="#fff" stroke-width="2.5"/></svg></div>
  <div class="svc-label abs" style="left:840px;width:200px;top:461px">Fence Staining</div>

  <div class="svc-label l abs" style="left:75px;width:250px;top:531px">Maid Services<br>House Cleaning</div>
  <div class="svc-icon" style="left:349px;top:517px"><svg width="24" height="30"><circle cx="10" cy="5" r="4" fill="#fff"/><path d="M4 30V14a6 5 0 0112 0v16z" fill="#fff"/><path d="M20 4v24" stroke="#fff" stroke-width="2"/></svg></div>

  <div class="svc-icon" style="left:832px;top:517px"><svg width="28" height="28"><path d="M4 24L24 4M6 4l18 20" stroke="#fff" stroke-width="3"/></svg></div>
  <div class="svc-label abs" style="left:915px;width:200px;top:531px">Landscaping<br>Services</div>

  <div class="svc-label l abs" style="left:75px;width:250px;top:612px">Commercial &amp;<br>Condominium &amp;<br>Apartment Painting</div>
  <div class="svc-icon" style="left:338px;top:621px"><svg width="26" height="28"><rect x="3" y="3" width="20" height="23" fill="none" stroke="#fff" stroke-width="2.5"/><path d="M8 9h3M15 9h3M8 15h3M15 15h3" stroke="#fff" stroke-width="2.5"/></svg></div>

  <div class="svc-icon" style="left:842px;top:621px"><svg width="26" height="26"><rect x="3" y="3" width="20" height="20" fill="none" stroke="#fff" stroke-width="2.5"/><path d="M13 3v20M3 13h20" stroke="#fff" stroke-width="2.5"/></svg></div>
  <div class="svc-label abs" style="left:920px;width:200px;top:640px">Window<br>Washing</div>

  <div class="center-name abs">BRINDLE</div>
</section>

<section class="gallery">
  <h2 class="abs">Photo Inspiration <span>Gallery</span></h2>
  <p class="abs">At BRINDLE we understand the importance of home and family. We work to ensure your home is beautiful and it is protected for generations.</p>
  <div class="tile" style="left:99px;top:257px;background:linear-gradient(#7a8f5a,#3d5226)" role="img" aria-label="Gardener weeding a lawn">
    <div class="tile-overlay"><h3>Landscaping<br>weeding</h3><p>Lorem ipsum dolor sit amet, more consectetuer adipiscing elit.</p><span class="plus"></span></div>
  </div>
  <div class="tile" style="left:434px;top:257px;background:linear-gradient(#e6dccb,#a07a4f)" role="img" aria-label="Empty living room with hardwood floors, fireplace and chandelier"></div>
  <div class="tile" style="left:768px;top:257px;background:linear-gradient(#9ec3e6,#b26a43 60%,#7a4a32)" role="img" aria-label="Victorian house facade with paint colour swatches"></div>
  <div class="tile" style="left:99px;top:564px;background:linear-gradient(#e9eef2,#c9a98b)" role="img" aria-label="Happy family of four smiling together at home"></div>
  <div class="tile" style="left:434px;top:564px;background:linear-gradient(#6a9a4a,#a8433a 55%,#3f6a2c)" role="img" aria-label="Freshly planted flower bed along a garden path"></div>
  <div class="tile" style="left:768px;top:564px;background:linear-gradient(#bfc6cc,#8a8276)" role="img" aria-label="Stone house exterior with window and roof trim"></div>
  <div class="btn btn-blue" style="left:535px;top:896px;width:130px;justify-content:center;gap:14px">View All <i><svg width="8" height="10"><path d="M1 1l5 4-5 4" fill="none" stroke="#fff" stroke-width="2"/></svg></i></div>
</section>

<section class="testimonial" role="img" aria-label="Grayscale collage of satisfied client portraits">
  <h2 class="abs">Brindle Partner Experience</h2>
  <div class="avatar abs" role="img" aria-label="Client portrait"></div>
  <p class="quote abs"><b>“</b>Their team was pleasant and very professional to work with, they showed up each morning and cleaned up after themselves each day they worked. I strongly recommend Cedar Ridge for any landscaping or hardscaping work <b>”</b></p>
  <div class="author abs">- Martin L.</div>
  <div class="dots abs"><span></span><span></span><span></span></div>
</section>

<nav class="bottom-nav">
  <a style="left:275px">Home</a>
  <a style="left:418px">About</a>
  <a style="left:554px">Who We Are</a>
  <a style="left:718px">Gallery</a>
  <a style="left:845px">Contact Us</a>
</nav>

<footer class="site-footer">
  <h4 style="left:100px">Quick Links</h4>
  <ul class="quick-links abs">
    <li>What We Do</li>
    <li>Our Promise</li>
    <li>Client Experiences</li>
    <li>Promotions</li>
    <li>Career Opportunities / Join The Team</li>
  </ul>
  <h4 style="left:338px">Contact Info</h4>
  <div class="info-row" style="top:80px"><svg width="14" height="20"><path d="M7 0a7 7 0 017 7c0 5-7 13-7 13S0 12 0 7a7 7 0 017-7z" fill="#3d8fd8"/><circle cx="7" cy="7" r="2.5" fill="#1d1d1d"/></svg><div>Brindle residential services<br>Lorem ipsum dolor sit amet.</div></div>
  <div class="info-row" style="top:140px"><svg width="14" height="14" viewBox="0 0 24 24"><path fill="#3d8fd8" d="M6.6 10.8a15 15 0 006.6 6.6l2.2-2.2c.3-.3.7-.4 1-.2 1.1.4 2.3.6 3.6.6.6 0 1 .4 1 1V20c0 .6-.4 1-1 1A17 17 0 013 4c0-.6.4-1 1-1h3.5c.6 0 1 .4 1 1 0 1.3.2 2.5.6 3.6.1.3 0 .7-.2 1z"/></svg><div>555.010.2384</div></div>
  <div class="info-row" style="top:180px"><svg width="16" height="12"><rect x="0" y="0" width="16" height="12" rx="2" fill="#3d8fd8"/><path d="M1 1l7 5 7-5" fill="none" stroke="#1d1d1d"/></svg><div>hello@brindlehomeworks.example</div></div>
  <h4 style="left:655px">Subscribe Newsletter</h4>
  <div class="newsletter-note abs">Get The Latest Updates By Entering Your Email Address</div>
  <svg class="abs" style="left:850px;top:84px" width="36" height="28"><path d="M2 14L34 2 24 26 18 16z" fill="var(--green)"/></svg>
  <div class="newsletter abs"><div class="input">Please Type Here</div><div class="go">Subscribe</div></div>
  <div class="foot-brand abs">
    <div class="name">BRINDLE</div>
    <div class="social"><span></span><span></span><span></span><span></span></div>
  </div>
</footer>

<div class="copyright abs" style="left:0;width:1200px">Copyright © 2016. Brindle residential services. All Rights Reserved</div>

</body>
</html>
```